Professional Service Proposal for a Technical Recruiting Company

My firm, RVL Technology, has been asked to submit a proposal for a large recruiting effort to a perspective client. I have attached the draft outline of the content, pictures of our team, and our logo files. I am looking for help turning this into a professional looking proposal that helps us win the work!NOTE:The attached document is just an outline. I tried to separate pages by stating "PAGE BREAK." Titles are underlined. That said, you have the flexibility to do what you want to make it look good!

Industry/Entity Type

Information Technology

Font styles to use
Sans Serif

Colors

Designer to choose colors to be used in the design.

Requirements
Must have
• Use of our logo
• Use of our color scheme (or colors that go well with our logo)
• Clean, crisp lay out
• Graphics and images where applicable
• Easy to edit format. I will be changing the wording!

```html
<!DOCTYPE html>
<html lang="en">
<head>
<meta charset="utf-8">
<title>RVL Technology – Project-Based Recruiting Proposal</title>
<link rel="stylesheet" href="https://fonts.googleapis.com/css2?family=Exo+2:wght@500;600;700;800&family=Open+Sans:wght@400;600;700&display=swap">
<style>
:root{
  --navy:#231c7d;
  --navy-deep:#1b1566;
  --orange:#f04e14;
  --white:#ffffff;
  --ink:#333340;
  --backdrop:#d6d6d6;
  --label:#27247a;
}
*{box-sizing:border-box;margin:0;padding:0}
html,body{width:1200px;height:1048px;overflow:hidden;background:var(--backdrop)}
body{position:relative;font-family:"Open Sans",Arial,sans-serif;color:var(--ink)}
.page-label{position:absolute;width:317px;text-align:center;font-family:"Open Sans",Arial,sans-serif;font-size:22px;color:var(--label)}
.page{position:absolute;width:317px;height:443px;background:var(--white);overflow:hidden;box-shadow:0 3px 10px rgba(0,0,0,.25)}
.page svg.bg{position:absolute;inset:0}
.abs{position:absolute}
.head{font-family:"Exo 2",Arial,sans-serif;font-weight:700}
.orange{color:var(--orange)}
.navy{color:var(--navy)}
.small{font-size:5px;line-height:1.45;text-align:justify}

/* cover */
.brand{display:flex;align-items:center;gap:7px;font-family:"Exo 2",Arial,sans-serif;font-weight:800;color:var(--navy)}
.brand-dot{width:34px;height:34px;border-radius:50%;background:var(--orange)}
.cover-brand{left:32px;top:62px;font-size:44px}
.cover-title{left:36px;top:286px;color:var(--white);font-size:27px;line-height:1.33;letter-spacing:-.2px}
.cover-bar{left:36px;top:403px;width:281px;height:27px;background:var(--navy);color:var(--white);font-family:"Exo 2",Arial,sans-serif;font-weight:600;font-size:13.5px;line-height:27px;padding-left:13px}

/* index */
.index-title{left:27px;top:27px;font-size:17px;font-weight:600;color:var(--orange);font-family:"Exo 2",Arial,sans-serif}
.index-rule{left:90px;top:37px;width:227px;height:2px;background:var(--navy)}

/* about */
.about-head{left:0;top:18px;width:317px;text-align:center}
.about-head .line1{color:var(--white);font-size:24px}
.about-head .line2{color:var(--orange);font-size:17.5px;line-height:1.3}
.section-title{left:25px;width:267px;display:flex;align-items:center;gap:6px;font-family:"Exo 2",Arial,sans-serif;font-weight:700;font-size:8.5px;color:var(--navy)}
.section-title::before,.section-title::after{content:"";flex:1;height:1px;background:var(--navy)}
.section-text{left:16px;width:285px}
.values{left:52px;top:413px;display:flex;gap:12px;font-size:5px;font-style:italic}
.values span::before{content:"";display:inline-block;width:4px;height:4px;border-radius:50%;background:var(--navy);margin-right:4px;vertical-align:middle}

/* team */
.team-band{left:0;top:21px;width:264px;height:28px;background:var(--orange)}
.team-title{left:19px;top:27px;font-size:16px;color:var(--navy)}
.team-badge{right:22px;top:8px;font-size:15px;gap:3px}
.team-badge .brand-dot{width:44px;height:44px;background:var(--white);border:3px solid var(--orange);display:flex;align-items:center;justify-content:center}
.member{left:19px;width:282px;display:flex;gap:14px}
.portrait{flex:0 0 58px;height:74px;background:linear-gradient(180deg,#c7c1bb,#6f6862)}
.member h3{font-family:"Exo 2",Arial,sans-serif;font-size:9px;font-weight:700;color:var(--orange)}
.member h4{font-family:"Exo 2",Arial,sans-serif;font-size:8.5px;font-weight:500;color:var(--navy);margin-bottom:3px}
.team-foot{left:0;bottom:0;width:317px;height:10px;background:var(--navy)}

/* testimonial */
.quote-photo{left:0;top:0;width:317px;height:300px;background:linear-gradient(160deg,#5b55b8 0%,#3d3796 55%,#2a2480 100%)}
.quote-head{left:0;top:178px;width:317px;text-align:center;font-size:24px;line-height:1.3}
.quote-text{left:36px;top:326px;width:260px;font-size:8px;line-height:1.4;text-align:justify;color:#222}
.quote-mark{left:24px;top:322px;font-size:14px;font-weight:700;color:#222}
.quote-by{left:36px;top:408px;font-size:8px;font-weight:600;color:var(--navy)}

/* case study */
.case-photo{left:0;top:0;width:317px;height:199px;background:linear-gradient(135deg,#f3f3f6 0%,#d9dce4 50%,#b9a58f 100%)}
.case-brand{left:30px;top:180px;font-size:26px;gap:4px}
.case-brand .brand-dot{width:24px;height:24px}
.engine-title{left:17px;top:236px;color:var(--white);font-size:14px;line-height:1.28}
.engine-text{left:17px;top:295px;width:120px;color:var(--white);font-size:4.5px;line-height:1.45}
.engine-text b{display:block;margin-top:5px;font-size:5px}
.wars-title{left:192px;top:204px;color:var(--white);font-size:14.5px;line-height:1.3}
.wars-text{left:192px;top:250px;width:112px;color:var(--white);font-size:4.8px;line-height:1.42;text-align:justify}
.goal{top:392px;color:var(--white);font-size:4.6px;line-height:1.45}
.goal b{display:block;font-size:5px;margin-bottom:2px}
</style>
</head>
<body>

<div class="page-label" style="left:124px;top:18px">Page 1</div>
<div class="page-label" style="left:480px;top:12px">Page 2</div>
<div class="page-label" style="left:834px;top:14px">Page 3</div>
<div class="page-label" style="left:124px;top:520px">Page 4</div>
<div class="page-label" style="left:480px;top:520px">Page 5</div>
<div class="page-label" style="left:834px;top:524px">Page 6</div>

<!-- Cover -->
<section class="page cover" style="left:124px;top:58px">
  <svg class="bg" width="317" height="443" viewBox="0 0 317 443">
    <polygon points="267,0 317,0 317,443 0,443 0,205 100,258 267,170" fill="var(--orange)"/>
  </svg>
  <div class="abs brand cover-brand"><span class="brand-dot"></span>RVL</div>
  <h1 class="abs head cover-title">RVL TECHNOLOGY<br>PROJECT-BASED<br>RECRUITING</h1>
  <div class="abs cover-bar">Specifically prepared for CLIENT, Inc.</div>
</section>

<!-- Index -->
<section class="page index" style="left:480px;top:58px">
  <div class="abs index-title">Index</div>
  <div class="abs index-rule"></div>
</section>

<!-- About -->
<section class="page about" style="left:834px;top:58px">
  <svg class="bg" width="317" height="443" viewBox="0 0 317 443">
    <polygon points="0,0 317,0 317,120 158,142 0,120" fill="var(--navy)"/>
    <rect x="0" y="428" width="317" height="15" fill="var(--orange)"/>
  </svg>
  <div class="abs about-head head">
    <div class="line1">RVL:</div>
    <div class="line2">INNOVATIVE HIRING PRACTICES<br>THAT SCALE</div>
  </div>
  <div class="abs section-title" style="top:137px">ABOUT <span class="orange">US</span></div>
  <p class="abs section-text small" style="top:158px">RVL Technology is a Virginia-based talent acquisition consultancy helping to bring innovative technology to market by providing the sector's most innovative and disruptive firms the talent they need to scale.<br><br>With an average tenure of 12 years in talent acquisition, and experience that ranges from the capital to the west coast, our team is uniquely qualified to deliver on our client's needs. We have worked with passionate founders looking to add their first engineers, built teams of 50+ for large government contractors, and scaled venture-backed SaaS start-ups to their IPO.<br>The RVL team is here to help you address the problems you know you have and those you haven't seen coming yet.</p>
  <div class="abs section-title" style="top:249px">WHY WE <span class="orange">EXIST</span></div>
  <p class="abs section-text small" style="top:270px">RVL Technology was founded for one purpose – to drive tech advancement by providing the sector's most innovative firms with the talent they need to scale. We design and deliver custom talent acquisition strategies for the most innovative and driven technology companies on the market.</p>
  <div class="abs section-title" style="top:321px">WHAT WE ARE <span class="orange">AFTER</span></div>
  <p class="abs section-text small" style="top:342px">RVL Technology was founded for one purpose – to drive tech advancement by providing the sector's most innovative firms with the talent they need to scale. We design and deliver custom talent acquisition strategies for the most innovative and driven technology companies on the market.</p>
  <div class="abs section-title" style="top:389px">WHAT WE <span class="orange">BELIEVE IN</span></div>
  <div class="abs values"><span>Buy-in</span><span>Intellectual Curiosity</span><span>Reliability</span><span>Integrity</span></div>
</section>

<!-- Team -->
<section class="page team" style="left:124px;top:565px">
  <div class="abs team-band"></div>
  <h2 class="abs head team-title">OUR <span style="color:var(--white)">TEAM</span></h2>
  <div class="abs brand team-badge"><span class="brand-dot">RVL</span></div>

  <article class="abs member" style="top:70px">
    <div class="portrait" role="img" aria-label="Portrait photo of Daniel Corwin"></div>
    <div><h3>DANIEL CORWIN</h3><h4>Account Lead</h4>
    <p class="small">The only thing that excites Daniel more than entrepreneurialism is the people behind disruptive companies. After 6 years building teams as large as 65 for federal IT contractors, Daniel started RVL to better serve the sector's most promising firms. Daniel will be responsible for daily management of this project, including interviewing key candidates, coaching hiring managers and working with stakeholders on the backlog.</p></div>
  </article>
  <article class="abs member" style="top:163px">
    <div class="portrait" role="img" aria-label="Portrait photo of Peter Halvorsen"></div>
    <div><h3>PETER HALVORSEN</h3><h4>Director, Candidate Delivery</h4>
    <p class="small">If there is one thing Peter knows, it is how to build and scale recruiting operations. Peter has been fortunate enough to experience 3 successful exits as part of the leadership teams for fast-growing technology startups. Peter will be responsible for keeping the client recruiting engine humming throughout this project and will be available for monthly performance reviews, candidate messaging strategy sessions and process tweaks.</p></div>
  </article>
  <article class="abs member" style="top:268px">
    <div class="portrait" role="img" aria-label="Portrait photo of Laura Mendez"></div>
    <div><h3>LAURA MENDEZ</h3><h4>Senior Recruiter</h4>
    <p class="small">A 15-year veteran of the talent acquisition industry, Laura has worked both as an agency recruiter and as an internal resource for large consulting and financial firms. This experience makes Laura a valuable asset to anyone looking to revamp their internal hiring practice. Laura will be responsible for managing the sourcing team, interviewing key candidates and maintaining quality as the project speeds up.</p></div>
  </article>
  <article class="abs member" style="top:357px">
    <div class="portrait" role="img" aria-label="Portrait photo of Sofia Reyes"></div>
    <div><h3>SOFIA REYES</h3><h4>Jr. Recruiter/Account Coordinator</h4>
    <p class="small">A new addition to the RVL team, Sofia brings a wealth of experience in process improvement, stakeholder management and corporate communication. For this project, she will be responsible for tracking and reporting key metrics, managing communication and scheduling across hiring managers, and assisting with candidate onboarding.</p></div>
  </article>
  <div class="abs team-foot"></div>
</section>

<!-- Testimonial -->
<section class="page testimonial" style="left:480px;top:565px">
  <div class="abs quote-photo" role="img" aria-label="Photo of a smiling business team holding a laptop, tinted blue"></div>
  <svg class="bg" width="317" height="443" viewBox="0 0 317 443">
    <polygon points="0,280 317,238 317,262 0,312" fill="var(--orange)"/>
    <polygon points="0,312 317,262 317,443 0,443" fill="var(--white)"/>
  </svg>
  <h2 class="abs head quote-head"><span style="color:var(--white)">WHAT OUR CLIENTS</span><br><span class="orange">HAVE TO SAY</span></h2>
  <div class="abs quote-mark">“</div>
  <p class="abs quote-text">Through our partnership with RVL Technology, we have been able to grow our software development practice by more than 120% this year. Knowing that we can grow quickly, without sacrificing quality, has allowed us to focus on what we do best –delivering critical software solutions to our customers. <b>”</b></p>
  <div class="abs quote-by">-Marcus Ellery, President of Brightfold Corp.</div>
</section>

<!-- Case study -->
<section class="page case" style="left:834px;top:565px">
  <div class="abs case-photo" role="img" aria-label="Photo of two colleagues pointing at a rising growth chart on a whiteboard"></div>
  <svg class="bg" width="317" height="443" viewBox="0 0 317 443">
    <polygon points="0,175 150,168 162,225 0,226" fill="var(--white)"/>
    <polygon points="0,226 115,226 150,365 0,365" fill="var(--navy)"/>
    <polygon points="158,190 317,175 317,360 175,360" fill="var(--orange)"/>
    <rect x="0" y="363" width="317" height="80" fill="var(--navy)"/>
  </svg>
  <div class="abs brand case-brand"><span class="brand-dot"></span>RVL</div>
  <h2 class="abs head engine-title">BUILD A<br>WINNING<br>TALENT ENGINE</h2>
  <div class="abs engine-text">Our objective is to design and implement a talent acquisition program that effectively captures top platform consultants and brings them into the client integration ecosystem as a member of the team. There are three main goals.
    <b>GROWTH GOAL:</b>Identify, hire and on-board approximately 500 new client consultants by September. It is anticipated that these hires will be distributed across each of the client's standard employee tiers.</div>
  <h2 class="abs head wars-title">CORELANE<br>TALENT WARS</h2>
  <p class="abs wars-text">CLIENT's growth to-date has been impressive. The firm has seen a 188% increase in headcount in the past two years, growing by an average of 40 FTE annually. Unfortunately, the current strategy of organic growth led by static job postings and internal employee referrals has reached a saturation point. In an industry where average Gross Profit Per Consultant hovers around XXXX, it is simply not possible to keep up with client demand without a more dynamic talent acquisition process.</p>
  <div class="abs goal" style="left:17px;width:95px"><b>FINANCIAL GOAL:</b>Achieve a cost-per-hire (CPH) of less than $9,000.</div>
  <div class="abs goal" style="left:145px;width:160px;text-align:justify"><b>SUSTAINABILITY GOAL:</b>Ingrain intentional, thoughtful talent acquisition best practices into the client's management culture and provide the firm with the tools and processes necessary to continue to build on its success, including structured interviews, a candidate database and a clear onboarding program with metrics.</div>
</section>

</body>
</html>
```